TR Ingotvale Corporate Letterhead

I have a corporate logo (uploaded). However, it may not be high enough quality for printing purposes, so the logo may need some work. I have a sample of letterhead (uploaded) that we currently use for electronic purposes only. The new design for letterhead does NOT need to look like the current electronic version -- in fact, I would prefer it doesn't. Additionally, I would like to be able to print this through pelkaprint.com. If your design includes something on the reverse side of the paper, that's okay (even cool!) -- pelkaprint.com can easily handle the printing of this. In summary I would like a letterhead design for print purposes, as well as an electronic version of the letterhead (to replace our current version) that can be used with Microsoft Word. Also, if you want to see how the logo on our website looks, go to www.tringotvale.com.

Requirements
Must have
• At least the front side of a letterhead design using our current logo. A backside of the letterhead is optional. Must be able to print through pelkaprint.com. Also must have an electronic version of the final design to use with Microsoft Word. Also, if the logo I uploaded isn't high enough quality, the logo will need to be enhanced for printing purposes. The color that I picked on ArtHively's color wheel may not be the correct blue, so feel free to change that if necessary. Also, the address and website address can be in a contrasting color chosen by the designer.
Nice to have
• I like original ideas/designs. So have fun with it!
Should not have
• Colors that are not in our current logo. If you would like to view it on our website, got to www.tringotvale.com

```html
<!DOCTYPE html>
<html lang="en">
<head>
<meta charset="utf-8">
<title>TR Ingotvale Letterhead</title>
<link rel="stylesheet" href="https://fonts.googleapis.com/css2?family=Montserrat:wght@400;500&display=swap">
<style>
  :root {
    --brand-blue: #2a74b6;
    --paper: #ffffff;
    --backdrop: #e8ebea;
    --text-light: #ffffff;
  }
  html, body {
    margin: 0;
    padding: 0;
    width: 1200px;
    height: 1058px;
    overflow: hidden;
    background: var(--backdrop);
  }
  .letterhead {
    position: absolute;
    left: 213px;
    top: 29px;
    width: 774px;
    height: 1000px;
    background: var(--paper);
    box-shadow: 0 4px 18px rgba(0,0,0,0.12);
  }
  .header-band {
    position: absolute;
    left: 0;
    top: 0;
    width: 774px;
    height: 70px;
  }
  .header-band path { fill: var(--brand-blue); }
  .company-name {
    position: absolute;
    left: 34px;
    top: 34px;
    margin: 0;
    font-family: "Montserrat", sans-serif;
    font-weight: 500;
    font-size: 28px;
    line-height: 1;
    color: var(--brand-blue);
  }
  .website {
    position: absolute;
    left: 356px;
    top: 50px;
    font-family: "Montserrat", sans-serif;
    font-weight: 400;
    font-size: 11px;
    line-height: 1;
    color: var(--text-light);
  }
  .address {
    position: absolute;
    left: 356px;
    top: 76px;
    font-family: "Montserrat", sans-serif;
    font-weight: 500;
    font-size: 12px;
    line-height: 1;
    color: var(--brand-blue);
  }
  .footer-rule {
    position: absolute;
    left: 0;
    bottom: 0;
    width: 100%;
    height: 7px;
    background: var(--brand-blue);
  }
</style>
</head>
<body>
  <main class="letterhead">
    <svg class="header-band" viewBox="0 0 774 70" aria-hidden="true">
      <path d="M0 0 H774 V70 H352 Q340 70 340 58 V40 Q340 26 326 26 H0 Z"/>
    </svg>
    <h1 class="company-name">TR Ingotvale</h1>
    <div class="website">www.tringotvale.com</div>
    <div class="address">4810 W. Harbor Parkway, Suite 300, Fairmont, TX 75012</div>
    <div class="footer-rule"></div>
  </main>
</body>
</html>
```